owlbrass website

commerce website to sell cookeries, brackets, mailboxes and to show off homes built. Modern Steel in design see tandra wheels web page to be like: https://www.tandrawheels.example/en/ sorry its net haven hosting word press divi

must be able to add products to page

Target Market(s)

mainly western states of U.S.

Industry/Entity Type

Building Product

Coding

Coded - Design and coding required

Number of Pages Required

3 page

Font styles to use
Sans Serif

Colors

Designer to choose colors to be used in the design.

Requirements
Must have
• customers to be able to order products from page
• net haven hosting word press divi

```html
<!DOCTYPE html>
<html lang="en">
<head>
<meta charset="utf-8">
<title>Owl Brass — Outdoor Fire Pits, Brackets and Mailboxes</title>
<link rel="stylesheet" href="https://fonts.googleapis.com/css2?family=Exo+2:wght@500;600&family=Lato:wght@400;700&display=swap">
<style>
:root{
  --brand:#4f6290;
  --brand-dark:#3f5079;
  --ink:#111318;
  --muted:#6b6f78;
  --panel:#edeef2;
  --panel-soft:#f1f2f5;
  --line:#d7d9df;
  --white:#ffffff;
  --footer:#1d2231;
  --footer-deep:#14192a;
}
*{box-sizing:border-box;margin:0;padding:0}
html,body{width:1200px;height:4138px;overflow:hidden;background:var(--white)}
body{position:relative;font-family:"Lato",sans-serif;color:var(--ink)}
.abs{position:absolute}
.heading{font-family:"Exo 2",sans-serif;font-weight:600;color:var(--ink);letter-spacing:-.3px}
.rule{position:absolute;height:2px;background:linear-gradient(90deg,transparent,var(--brand) 40%,var(--brand))}
.body-text{font-size:12px;line-height:19.5px;color:var(--muted)}
.btn{position:absolute;display:flex;align-items:center;justify-content:center;gap:10px;background:var(--brand);color:var(--white);font-size:13.5px;font-weight:700;box-shadow:0 4px 10px rgba(79,98,144,.25)}
.btn-outline{background:var(--white);color:var(--brand);border:1.5px solid var(--brand);box-shadow:none}
.photo{position:absolute}
.dot{position:absolute;width:9px;height:9px;border-radius:50%;border:1.5px solid var(--brand)}
.dot.on{background:var(--brand)}

/* header */
.logo-box{left:0;top:0;width:365px;height:135px;background:var(--brand);display:flex;align-items:center;justify-content:center;gap:10px}
.logo-box .mark{width:14px;height:14px;border-radius:50%;background:var(--white)}
.logo-box .name{font-family:"Exo 2",sans-serif;font-weight:500;font-size:24px;color:var(--white);letter-spacing:.5px}
.nav-signin{left:875px;top:36px;font-size:13px;color:var(--brand);font-weight:700}
.nav-signup{left:948px;top:27px;width:91px;height:36px;font-size:13px;border-radius:3px}
.social-rail{left:1128px;width:36px;height:36px;border-radius:4px;background:var(--white);box-shadow:0 2px 8px rgba(0,0,0,.07);display:flex;align-items:center;justify-content:center}
.social-rail span{width:8px;height:8px;border-radius:50%;background:#c9ccd6}
.social-rail.active span{background:var(--brand)}

/* hero */
.hero-title{left:163px;top:238px;font-size:55px;line-height:64px}
.hero-text{left:163px;top:378px;width:420px;font-size:13px;line-height:21px;color:var(--muted)}

/* products */
.card{position:absolute;width:227px;height:226px;background:var(--white);box-shadow:0 0 0 5px var(--panel-soft),0 2px 10px rgba(0,0,0,.06)}
.card .photo{left:8px;top:8px;right:8px;bottom:8px}
.prod-name{position:absolute;width:227px;text-align:center;font-family:"Exo 2",sans-serif;font-weight:600;font-size:17px}
.prod-price{position:absolute;width:227px;text-align:center;font-size:14px;color:var(--brand)}
.prod-price b{color:var(--ink)}

/* inputs */
.field{position:absolute;height:44px;border:1px solid var(--line);font-size:11.5px;color:var(--muted);padding:15px 18px}

/* footer */
.footer{left:0;top:3768px;width:1200px;height:323px;background:radial-gradient(ellipse at 20% 30%,#2b3347,var(--footer) 55%,var(--footer-deep))}
.footer-logo{left:0;top:3820px;width:1200px;display:flex;flex-direction:column;align-items:center;gap:10px}
.footer-logo .mark{width:22px;height:22px;border-radius:50%;background:var(--white)}
.footer-logo .name{font-family:"Exo 2",sans-serif;font-weight:500;font-size:26px;color:var(--white);letter-spacing:.5px}
.footer-nav{left:0;top:3925px;width:1200px;display:flex;justify-content:center;gap:20px;font-size:11px;color:#dfe2ea}
.footer-line{left:161px;top:3970px;width:878px;height:1px;background:rgba(255,255,255,.2)}
.contact-icon{position:absolute;top:4011px;width:38px;height:38px;border:1px solid rgba(255,255,255,.7);display:flex;align-items:center;justify-content:center}
.contact-text{position:absolute;font-size:11px;line-height:17px;color:#e3e6ee}
.foot-social{position:absolute;top:4011px;width:37px;height:37px;border:1px solid rgba(255,255,255,.7);display:flex;align-items:center;justify-content:center}
.foot-social span{width:9px;height:9px;background:var(--white)}
.foot-social.active{background:var(--white)}
.foot-social.active span{background:var(--brand)}
.copyright{left:0;top:4091px;width:1200px;height:47px;background:var(--brand);color:#e9ecf4;font-size:11px;display:flex;align-items:center;justify-content:center}
</style>
</head>
<body>

<!-- Header -->
<div class="abs logo-box"><span class="mark"></span><span class="name">OWL BRASS</span></div>
<div class="photo" style="left:622px;top:0;width:465px;height:638px;background:radial-gradient(ellipse at 50% 60%,#3a3f48 0 28%,#efeff0 29%)" role="img" aria-label="Black steel chimney fire pit with burning logs on three legs"></div>
<div class="abs nav-signin">Sign In</div>
<div class="btn nav-signup">Sign Up</div>
<svg class="abs" style="left:1134px;top:36px" width="28" height="32" viewBox="0 0 28 32" aria-label="Cart, 2 items">
  <text x="16" y="9" font-size="8" font-family="Lato" font-weight="700" fill="#4f6290">2</text>
  <path d="M2 12h4l4 12h12l3-9H8" fill="none" stroke="#4f6290" stroke-width="2.4" stroke-linejoin="round"/>
  <circle cx="12" cy="28" r="2" fill="#4f6290"/><circle cx="21" cy="28" r="2" fill="#4f6290"/>
</svg>
<div class="abs social-rail" style="top:183px"><span></span></div>
<div class="abs social-rail active" style="top:247px"><span></span></div>
<div class="abs social-rail" style="top:310px"><span></span></div>
<div class="abs social-rail" style="top:372px"><span></span></div>
<div class="dot" style="left:1141px;top:529px"></div>
<div class="dot on" style="left:1141px;top:568px"></div>
<div class="dot" style="left:1141px;top:606px"></div>

<!-- Hero -->
<div class="rule" style="left:165px;top:224px;width:145px"></div>
<h1 class="abs heading hero-title">Owl Brass<br>Outdoor Fire Pit</h1>
<p class="abs hero-text">Lorem Ipsum is simply dummy text of the printing and typesetting industry. Lorem Ipsum has been the industry's standard dummy text.</p>
<div class="btn" style="left:161px;top:466px;width:204px;height:51px;font-size:17px;font-weight:400">Add To Cart
  <svg width="24" height="22" viewBox="0 0 24 22"><path d="M1 3h4l3 11h11l3-8H6" fill="none" stroke="#fff" stroke-width="2"/><circle cx="10" cy="19" r="1.8" fill="#fff"/><circle cx="18" cy="19" r="1.8" fill="#fff"/></svg>
</div>

<!-- About -->
<div class="abs" style="left:438px;top:765px;width:762px;height:525px;background:var(--panel)"></div>
<div class="abs" style="left:247px;top:1047px;width:92px;height:143px;background:var(--panel-soft)"></div>
<div class="abs" style="left:488px;top:999px;width:100px;height:151px;background:var(--white)"></div>
<div class="photo" style="left:215px;top:904px;width:95px;height:143px;background:linear-gradient(135deg,#e4e6ee,#b7bcc9)" role="img" aria-label="Chrome wall hook fixture"></div>
<div class="abs" style="left:308px;top:817px;width:151px;height:208px;background:var(--brand)"></div>
<div class="photo" style="left:430px;top:850px;width:127px;height:149px;background:radial-gradient(circle at 50% 55%,#e8c21c 0 35%,#6b6a3a 36%,#3e4a2a)" role="img" aria-label="Yellow post box mounted outdoors"></div>
<div class="photo" style="left:339px;top:1028px;width:149px;height:209px;background:radial-gradient(ellipse at 50% 50%,#c9521c 0 18%,#2b2b2e 19%,#3a3a3c)" role="img" aria-label="Black steel lantern fireplace with fire"></div>
<div class="rule" style="left:731px;top:887px;width:90px"></div>
<h2 class="abs heading" style="left:710px;top:893px;font-size:35px">About Owl Brass</h2>
<p class="abs body-text" style="left:710px;top:938px;width:286px">Lorem Ipsum is simply dummy text of the printing and typesetting industry. Lorem Ipsum has been the industry's standard dummy text ever since the 1500s, when an unknown printer took a galley of type and scrambled it to make a type specimen book. It has survived not only five centuries, but also the leap into electronic typesetting, remaining essentially unchanged.</p>
<div class="btn" style="left:708px;top:1121px;width:121px;height:40px">Read More</div>

<!-- Products -->
<div class="rule" style="left:572px;top:1383px;width:83px"></div>
<h2 class="abs heading" style="left:0;top:1388px;width:1200px;text-align:center;font-size:35px">Owl Brass Products</h2>
<p class="abs body-text" style="left:375px;top:1432px;width:450px;text-align:center;font-size:11.5px">Lorem Ipsum is simply dummy text of the printing and typesetting industry. Lorem Ipsum has been the industry's standard dummy text ever since the 1500s.</p>

<div class="card" style="left:231px;top:1510px"><div class="photo" style="background:radial-gradient(ellipse at 50% 45%,#b07450 0 25%,#ecedf1 26%)" role="img" aria-label="Copper fire bowl on legs"></div></div>
<div class="card" style="left:487px;top:1510px"><div class="photo" style="background:radial-gradient(ellipse at 50% 50%,#2a2a2c 0 14%,#ecedf1 30%)" role="img" aria-label="Pair of black steel shelf brackets"></div></div>
<div class="card" style="left:742px;top:1510px"><div class="photo" style="background:radial-gradient(ellipse at 50% 50%,#1c1c1e 0 26%,#ecedf1 27%)" role="img" aria-label="Black steel mailbox with red flag"></div></div>

<div class="prod-name" style="left:231px;top:1764px">Steel Cookery</div>
<div class="prod-name" style="left:487px;top:1764px">Steel Bracket</div>
<div class="prod-name" style="left:742px;top:1764px">Steel Mailboxe</div>
<div class="prod-price" style="left:231px;top:1803px"><b>$</b> 45.50</div>
<div class="prod-price" style="left:487px;top:1803px"><b>$ 52.30</b></div>
<div class="prod-price" style="left:742px;top:1803px"><b>$</b> 120.42</div>
<p class="abs body-text" style="left:487px;top:1828px;width:227px;text-align:center;font-size:11px">Lorem Ipsum is simply dummy text of the printing and typesetting industry.</p>
<div class="rule" style="left:565px;top:1881px;width:90px"></div>
<div class="btn" style="left:490px;top:1908px;width:106px;height:42px;font-size:13px">Shop Now</div>
<div class="btn btn-outline" style="left:604px;top:1908px;width:104px;height:42px;font-size:13px">Add To Cart</div>

<!-- Special offers -->
<div class="photo" style="left:0;top:2041px;width:744px;height:524px;background:linear-gradient(160deg,#3a3530,#1f1d1b 45%,#2a2621)" role="img" aria-label="Dark wooden deck with a fire bowl at night"></div>
<h2 class="abs heading" style="left:163px;top:2178px;font-size:33px;line-height:42px;color:var(--white)">Our Special offers, 25% off<br>for Owl Brass Products</h2>
<p class="abs body-text" style="left:163px;top:2282px;width:405px;color:#e6e6e6;font-size:11.5px">Lorem Ipsum has been the industry's standard dummy text ever since the 1500s, when an unknown printer took a galley of type and scrambled it to make a type specimen book. It has survived not only five centuries, but also the leap into electronic typesetting, remaining essentially unchanged.</p>
<div class="btn" style="left:161px;top:2420px;width:119px;height:40px">Grab Now</div>
<div class="photo" style="left:647px;top:2075px;width:227px;height:225px;background:radial-gradient(ellipse at 50% 50%,#2c2c2e 0 22%,#ecedf1 36%)" role="img" aria-label="Two black articulating wall mount arms"></div>
<div class="abs" style="left:647px;top:2301px;width:97px;height:5px;background:#1d1d1f"></div>
<div class="photo" style="left:647px;top:2308px;width:227px;height:223px;background:radial-gradient(ellipse at 45% 50%,#3a3a3c 0 24%,#ecedf1 34%)" role="img" aria-label="Perforated steel fire pit with lid"></div>
<div class="photo" style="left:880px;top:2157px;width:227px;height:225px;background:radial-gradient(ellipse at 45% 50%,#d5231e 0 25%,#ecedf1 26%)" role="img" aria-label="Red post box with a letter"></div>
<div class="dot" style="left:934px;top:2423px"></div>
<div class="dot on" style="left:971px;top:2423px"></div>
<div class="dot" style="left:1008px;top:2423px"></div>

<!-- Customize -->
<div class="photo" style="left:355px;top:2722px;width:188px;height:225px;background:linear-gradient(180deg,#3b3b35 0,#e0641f 35%,#6b3a2c 60%,#f2ece8)" role="img" aria-label="Fire burning in a round steel bowl"></div>
<div class="photo" style="left:267px;top:2618px;width:171px;height:222px;background:linear-gradient(135deg,#c9cbe0,#a6a9c3);box-shadow:0 0 0 6px var(--white)" role="img" aria-label="Brass ring bracket on a wall"></div>
<div class="photo" style="left:161px;top:2803px;width:188px;height:223px;background:linear-gradient(180deg,#c9bfa9,#6f5b3e 45%,#4d6a32)" role="img" aria-label="Bronze pedestal mailbox in a garden"></div>
<div class="rule" style="left:636px;top:2651px;width:88px"></div>
<h2 class="abs heading" style="left:612px;top:2656px;font-size:35px">Customize Products</h2>
<p class="abs body-text" style="left:612px;top:2723px;width:310px">Lorem Ipsum is simply dummy text of the printing and typesetting industry. Lorem Ipsum has been the industry's standard dummy text ever since the 1500s, when an unknown printer took a galley of type and scrambled it to make a type specimen book. It has survived not only five centuries, but also the leap into electronic typesetting, remaining essentially unchanged.</p>
<div class="btn" style="left:610px;top:2892px;width:150px;height:41px">Customize Now</div>

<!-- Testimonial -->
<div class="abs" style="left:199px;top:3161px;width:802px;height:225px;background:var(--panel)"></div>
<div class="photo" style="left:748px;top:3048px;width:206px;height:338px;background:linear-gradient(180deg,#e9e6e3 0 18%,#2a2d36 40%,#1b1e26)" role="img" aria-label="Smiling businessman in a dark suit, arms crossed"></div>
<svg class="abs" style="left:236px;top:3204px" width="32" height="26" viewBox="0 0 32 26"><path d="M2 24V13C2 6 6 2 13 1v5c-4 1-5 3-5 7h5v11zM18 24V13c0-7 4-11 11-12v5c-4 1-5 3-5 7h5v11z" fill="#d3d5dc"/></svg>
<svg class="abs" style="left:655px;top:3330px" width="32" height="26" viewBox="0 0 32 26"><path d="M30 2v11c0 7-4 11-11 12v-5c4-1 5-3 5-7h-5V2zM14 2v11c0 7-4 11-11 12v-5c4-1 5-3 5-7H3V2z" fill="#d3d5dc"/></svg>
<p class="abs" style="left:289px;top:3212px;width:395px;font-size:12px;line-height:22.5px;color:#2a2d33">Lorem Ipsum is simply dummy text of the printing and typesetting industry. Lorem Ipsum has been the industry's standard dummy text ever since the 1500s, when an unknown printer took a galley of type and scrambled it to make a type specimen book. I</p>
<div class="abs" style="left:289px;top:3310px;font-size:12.5px;color:var(--muted)">Client Name</div>
<div class="abs" style="left:244px;top:3361px;width:149px;height:41px;background:var(--white)"></div>
<div class="dot" style="left:280px;top:3379px"></div>
<div class="dot on" style="left:317px;top:3379px"></div>
<div class="dot" style="left:354px;top:3379px"></div>

<!-- Newsletter -->
<h2 class="abs heading" style="left:0;top:3472px;width:1200px;text-align:center;font-size:33px">Subscribe To Our Newsletter</h2>
<p class="abs body-text" style="left:380px;top:3521px;width:440px;text-align:center;font-size:11.5px">Lorem Ipsum is simply dummy text of the printing and typesetting industry. Lorem Ipsum has been the industry's standard dummy text.</p>
<div class="field" style="left:369px;top:3586px;width:225px">Enter Name:</div>
<div class="field" style="left:605px;top:3586px;width:225px">Enter Email:</div>
<div class="btn" style="left:527px;top:3651px;width:149px;height:40px">Subscribe Now!</div>

<!-- Footer -->
<div class="abs footer"></div>
<div class="abs footer-logo"><span class="mark"></span><span class="name">OWL BRASS</span></div>
<nav class="abs footer-nav"><span>Home</span><span>About Us</span><span>Products</span><span>Home Builts</span><span>Contact Us</span></nav>
<div class="abs footer-line"></div>

<div class="contact-icon" style="left:161px">
  <svg width="18" height="18" viewBox="0 0 18 18"><path d="M4 1l3 4-2 2c1 2 3 4 5 5l2-2 4 3-2 3C8 16 2 10 1 4z" fill="none" stroke="#fff" stroke-width="1.4"/></svg>
</div>
<div class="contact-text" style="left:215px;top:4022px">+91-000-000-0000</div>
<div class="contact-icon" style="left:387px">
  <svg width="18" height="14" viewBox="0 0 18 14"><rect x="1" y="1" width="16" height="12" fill="none" stroke="#fff" stroke-width="1.4"/><path d="M1 1l8 7 8-7" fill="none" stroke="#fff" stroke-width="1.4"/></svg>
</div>
<div class="contact-text" style="left:440px;top:4022px">support@owlbrass.com</div>
<div class="contact-icon" style="left:610px">
  <svg width="14" height="18" viewBox="0 0 14 18"><path d="M7 17S1 10 1 6.5a6 6 0 0 1 12 0C13 10 7 17 7 17z" fill="none" stroke="#fff" stroke-width="1.4"/><circle cx="7" cy="6.5" r="2" fill="#fff"/></svg>
</div>
<div class="contact-text" style="left:665px;top:4013px;width:140px">100 Lorem ipsum is simply dummy text.</div>

<div class="foot-social" style="left:835px"><span></span></div>
<div class="foot-social active" style="left:888px"><span></span></div>
<div class="foot-social" style="left:941px"><span></span></div>
<div class="foot-social" style="left:994px"><span></span></div>

<div class="abs copyright">Copyright © 2020 Owl Brass. All Rights Reserved.</div>

</body>
</html>
```